New digital business consulting firm needs a professional Wordpress site

Lanternby Works Inc. is a new consulting firm that helps large companies with Digital Transformation. We help companies define a digital transformation strategy for improving the products, processes and customer journey using digital technology.

The website will serve three purposes:
1) Represent what the firm does.
2) Allow people to download research reports.
3) Collect email addresses from people who my be interested in using our services.

The tone of the website should be innovative and professional. The website will have only a few pages. You can see the type of content we wish to post on the current website www.lanternbyworks.example.

The website will support a book that is about to be released. The book cover is attached. However, the website does not necessarily have to match the book cover. Do not be constrained by the book cover.

Target Market(s)

Executives in large companies

Industry/Entity Type

Management Consulting

Font styles to use
Sans Serif

Requirements
Must have
• Professional and innovative, clean, cool
Nice to have
• None
Should not have
• None

```html
<!DOCTYPE html>
<html lang="en">
<head>
<meta charset="utf-8">
<title>Lanternby Works Inc.</title>
<link rel="stylesheet" href="https://fonts.googleapis.com/css2?family=Raleway:wght@300;400;500;600;700;800&display=swap">
<style>
:root{
  --navy:#0b1b5e;
  --navy-deep:#081650;
  --yellow:#fdd630;
  --ink:#333a4a;
  --grey-band:#eeeeee;
  --footer:#1b1b1b;
  --footer-text:#8b8b8b;
  --white:#ffffff;
}
*{margin:0;padding:0;box-sizing:border-box}
html,body{width:1200px;height:2462px;overflow:hidden}
body{font-family:"Raleway",Arial,sans-serif;color:var(--ink);background:var(--white);position:relative}
.abs{position:absolute}

.topbar{left:0;top:0;width:1200px;height:30px;background:var(--navy-deep);color:var(--white);font-size:11px;font-weight:600}
.topbar .phone{left:195px;top:8px;display:flex;align-items:center;gap:6px}
.topbar .address{right:197px;top:8px;display:flex;align-items:center;gap:6px}

.hero-photo{left:0;top:30px;width:1200px;height:733px;
  background:linear-gradient(90deg,#e9eef2 0%,#dfe5ea 30%,#c9a876 50%,#cfdcec 56%,#d6e2f1 75%,#c6d6ec 100%)}
.header{left:0;top:30px;width:1200px;height:95px;background:rgba(255,255,255,.93);box-shadow:0 1px 3px rgba(0,0,0,.12)}
.brand{left:197px;top:34px;font-size:26px;font-weight:700;color:var(--navy);letter-spacing:-.3px;display:flex;align-items:center;gap:8px}
.brand .dot{width:10px;height:10px;background:var(--yellow)}
.nav{left:545px;top:31px;display:flex;align-items:center;font-size:15px;font-weight:600;color:var(--navy)}
.nav a{color:inherit;text-decoration:none;padding:9px 22px;border-radius:2px}
.nav a.active{background:var(--yellow);padding:9px 22px}
.nav a:not(.active){padding:9px 0;margin-left:29px}

.hero-copy{left:678px;top:300px;color:var(--navy)}
.hero-copy .light{font-size:58px;font-weight:300;line-height:1;letter-spacing:-.5px}
.hero-copy .bold{font-size:60px;font-weight:700;line-height:1.05;letter-spacing:-.5px}
.hero-copy p{font-size:21px;font-weight:500;line-height:26px;width:330px;margin-top:26px}
.hero-arrow{top:421px;width:33px;height:33px;border:2px solid #a9b3bf;color:#a9b3bf;display:flex;align-items:center;justify-content:center;font-size:15px}

.btn{display:inline-flex;align-items:center;justify-content:space-between;background:var(--navy);color:var(--yellow);font-size:10px;font-weight:800;text-transform:uppercase;letter-spacing:.2px;border-radius:3px;height:35px;padding:0 14px 0 16px;gap:18px}
.btn svg{flex:none}

.signup{left:0;top:763px;width:1200px;height:86px;background:var(--yellow)}
.signup h3{left:202px;top:17px;font-size:21px;font-weight:700;color:var(--navy);line-height:26px;width:290px}
.signup .field{left:522px;top:25px;width:350px;height:36px;background:var(--white);border-radius:3px;font-size:13px;color:#555;padding:11px 14px}
.signup .btn{left:883px;top:25px;width:120px;height:36px}

.section-title{width:1200px;left:0;text-align:center;font-size:37px;font-weight:700;color:var(--navy);letter-spacing:-.3px}
.section-sub{width:1200px;left:0;text-align:center;font-size:13px;color:var(--ink)}

.item{width:210px}
.item .hex{position:absolute;left:0;top:0}
.item h4{position:absolute;left:72px;top:0;font-size:15px;font-weight:600;color:var(--navy);line-height:18px;width:170px}
.item p{position:absolute;left:72px;top:46px;font-size:12.5px;line-height:15px;color:var(--ink);width:170px}

.book-band{left:0;top:1277px;width:1200px;height:532px;background:var(--grey-band)}
.book-cover{left:268px;top:58px;width:274px;height:418px;background:linear-gradient(180deg,#0f1f66,#0a1850);border-left:14px solid var(--yellow);box-shadow:6px 16px 18px rgba(0,0,0,.28)}
.book-copy{left:579px;top:108px;width:390px;font-size:12.5px;line-height:15px;color:var(--ink)}
.book-copy h2{font-size:37px;font-weight:700;color:var(--navy);line-height:1;margin-bottom:20px;letter-spacing:-.3px}
.book-copy p{margin-bottom:15px}
.book-copy .btn{margin-top:26px;width:120px}

.dl .btn{position:absolute;left:72px;top:122px;width:120px}

.footer{left:0;top:2270px;width:1200px;height:192px;background:var(--footer);color:var(--footer-text)}
.footer h3{left:202px;top:25px;width:300px;font-size:21px;font-weight:500;line-height:26px;color:#b5b5b5}
.footer .tagline{left:202px;top:96px;width:310px;font-size:15px;line-height:19px}
.footer h5{font-size:12px;font-weight:700;color:#cfcfcf}
.footer .col{font-size:12px;line-height:15px}
.footer .social li{list-style:none;display:flex;align-items:center;gap:8px;margin-bottom:8px}
.footer .social .sq{width:13px;height:13px;background:var(--yellow)}
</style>
</head>
<body>

<div class="abs hero-photo" role="img" aria-label="Close-up photograph of a brass-rimmed wall clock face on the left, fading into a pale blue background"></div>

<div class="abs topbar">
  <div class="abs phone">
    <svg width="11" height="11" viewBox="0 0 24 24"><path fill="#fdd630" d="M6.6 10.8a15 15 0 0 0 6.6 6.6l2.2-2.2c.3-.3.7-.4 1-.2 1.1.4 2.3.6 3.6.6.6 0 1 .4 1 1V20c0 .6-.4 1-1 1A17 17 0 0 1 3 4c0-.6.4-1 1-1h3.5c.6 0 1 .4 1 1 0 1.3.2 2.5.6 3.6.1.3 0 .7-.2 1z"/></svg>
    555 014 2290
  </div>
  <div class="abs address">
    <svg width="10" height="13" viewBox="0 0 20 26"><path fill="#fdd630" d="M10 0a10 10 0 0 0-10 10c0 7.5 10 16 10 16s10-8.5 10-16A10 10 0 0 0 10 0zm0 14a4 4 0 1 1 0-8 4 4 0 0 1 0 8z"/></svg>
    48 Harrow Lane, Eastbrook, Canada
  </div>
</div>

<header class="abs header">
  <div class="abs brand"><span>lanternby works</span><span class="dot"></span></div>
  <nav class="abs nav">
    <a class="active">Home</a>
    <a>Book</a>
    <a>Services</a>
    <a>Downloadable Research</a>
  </nav>
</header>

<div class="abs hero-arrow" style="left:50px">&lt;</div>
<div class="abs hero-arrow" style="left:1120px">&gt;</div>

<div class="abs hero-copy">
  <div class="light">time to go</div>
  <div class="bold">digital</div>
  <p>We help companies establish a digital vision to thrive in the new era.</p>
  <div class="btn" style="margin-top:26px;width:120px">Know more
    <svg width="7" height="10" viewBox="0 0 7 10"><path d="M1 1l4 4-4 4" stroke="#fff" stroke-width="1.6" fill="none"/></svg></div>
</div>

<section class="abs signup">
  <h3 class="abs">Intrested to know how we can help you?</h3>
  <div class="abs field">Provide your E-mail address</div>
  <div class="abs btn">Subscribe
    <svg width="7" height="10" viewBox="0 0 7 10"><path d="M1 1l4 4-4 4" stroke="#fff" stroke-width="1.6" fill="none"/></svg></div>
</section>

<h2 class="abs section-title" style="top:898px">what we do</h2>
<p class="abs section-sub" style="top:951px">Our associate consultants, can be retained for the following services</p>

<div class="abs item" style="left:202px;top:1007px">
  <svg class="hex" width="60" height="54" viewBox="0 0 60 54"><path d="M16 2h28l14 25-14 25H16L2 27z" fill="none" stroke="#0b1b5e" stroke-width="2.5"/><circle cx="30" cy="27" r="11" fill="none" stroke="#0b1b5e" stroke-width="2.5"/><path d="M19 27h22M30 16v22" stroke="#0b1b5e" stroke-width="2"/></svg>
  <h4>Speaking Engagements</h4>
  <p>Provide an overview of the state of digital technology.</p>
</div>
<div class="abs item" style="left:473px;top:1007px">
  <svg class="hex" width="60" height="54" viewBox="0 0 60 54"><path d="M16 2h28l14 25-14 25H16L2 27z" fill="none" stroke="#0b1b5e" stroke-width="2.5"/><rect x="21" y="15" width="18" height="24" fill="none" stroke="#0b1b5e" stroke-width="2.5"/><path d="M25 21h10M25 26h10M25 31h6" stroke="#0b1b5e" stroke-width="2"/></svg>
  <h4>Digital Assessment</h4>
  <p>Help your company assess the state of your digital transformation.</p>
</div>
<div class="abs item" style="left:749px;top:1007px">
  <svg class="hex" width="60" height="54" viewBox="0 0 60 54"><path d="M16 2h28l14 25-14 25H16L2 27z" fill="none" stroke="#0b1b5e" stroke-width="2.5"/><rect x="27" y="15" width="16" height="12" fill="none" stroke="#0b1b5e" stroke-width="2.2"/><circle cx="20" cy="19" r="3" fill="#0b1b5e"/><path d="M20 23v13M16 28h8M27 28l-4-2" stroke="#0b1b5e" stroke-width="2.2"/></svg>
  <h4>Digital Strategy Development</h4>
  <p>Help define a digital vision and a strategy for implementation.</p>
</div>

<div class="abs btn" style="left:540px;top:1156px;width:120px">Our services
  <svg width="7" height="10" viewBox="0 0 7 10"><path d="M1 1l4 4-4 4" stroke="#fff" stroke-width="1.6" fill="none"/></svg></div>

<section class="abs book-band">
  <div class="abs book-cover" role="img" aria-label="Book cover of Leading Digital Well by Marcel Dufresne, navy with yellow title lettering"></div>
  <div class="abs book-copy">
    <h2>leading digital well</h2>
    <p>Our manual for winning in the next digital era.</p>
    <p>Its author, Marcel Dufresne, has been helping large companies establish and execute digital strategies for 25 years.</p>
    <p>It is critical for any executive in any function to understand key digital technologies, the way they are evolving, how companies can leverage them to improve products, processes, and the customer journey, and what kind of business outcomes can be derived.</p>
    <div class="btn">Buy the book
      <svg width="7" height="10" viewBox="0 0 7 10"><path d="M1 1l4 4-4 4" stroke="#fff" stroke-width="1.6" fill="none"/></svg></div>
  </div>
</section>

<h2 class="abs section-title" style="top:1874px">downloads</h2>
<p class="abs section-sub" style="top:1926px">Assess your digital maturity and disruption risk using a solid framework.</p>

<div class="abs item dl" style="left:202px;top:1993px">
  <svg class="hex" width="60" height="54" viewBox="0 0 60 54"><path d="M16 2h28l14 25-14 25H16L2 27z" fill="none" stroke="#0b1b5e" stroke-width="2.5"/><rect x="19" y="16" width="22" height="22" fill="#0b1b5e"/></svg>
  <h4>Customer Journey Assessment</h4>
  <p>Lorem ipsum dolor sit amet, consectetur adipiscing elit. Cras maximus tempus lacinia.</p>
  <div class="btn">Download
    <svg width="9" height="11" viewBox="0 0 9 11"><path d="M4.5 0v9M1 6l3.5 3.5L8 6" stroke="#fff" stroke-width="1.5" fill="none"/></svg></div>
</div>
<div class="abs item dl" style="left:473px;top:1993px">
  <svg class="hex" width="60" height="54" viewBox="0 0 60 54"><path d="M16 2h28l14 25-14 25H16L2 27z" fill="none" stroke="#0b1b5e" stroke-width="2.5"/><rect x="19" y="16" width="22" height="22" fill="#0b1b5e"/></svg>
  <h4>Operational Processes Assessment</h4>
  <p>Vivamus sagittis ante justo, ut malesuada quam tempor sit amet.</p>
  <div class="btn">Download
    <svg width="9" height="11" viewBox="0 0 9 11"><path d="M4.5 0v9M1 6l3.5 3.5L8 6" stroke="#fff" stroke-width="1.5" fill="none"/></svg></div>
</div>
<div class="abs item dl" style="left:749px;top:1993px">
  <svg class="hex" width="60" height="54" viewBox="0 0 60 54"><path d="M16 2h28l14 25-14 25H16L2 27z" fill="none" stroke="#0b1b5e" stroke-width="2.5"/><rect x="19" y="16" width="22" height="22" fill="#0b1b5e"/></svg>
  <h4>Product &amp; Services Assessment</h4>
  <p>Quisque ipsum urna, iaculis nec mattis non, faucibus in leo. Sed quis mattis mi, posuere viverra lorem.</p>
  <div class="btn">Download
    <svg width="9" height="11" viewBox="0 0 9 11"><path d="M4.5 0v9M1 6l3.5 3.5L8 6" stroke="#fff" stroke-width="1.5" fill="none"/></svg></div>
</div>

<footer class="abs footer">
  <h3 class="abs">How to put digital technology into business use?</h3>
  <p class="abs tagline">Make products smarter, operational processes more efficient, and the customer journey easier.</p>
  <div class="abs col" style="left:599px;top:35px">
    <h5>Get in touch with us</h5>
    <p style="margin-top:16px">48 Harrow Lane,<br>Eastbrook Park,<br>Canada.</p>
    <p style="margin-top:16px">Call: 555 014 2290</p>
  </div>
  <div class="abs col" style="left:821px;top:35px">
    <h5>Connect with us</h5>
    <ul class="social" style="margin-top:11px">
      <li><span class="sq"></span>Social Page</li>
      <li><span class="sq"></span>Updates</li>
      <li><span class="sq"></span>Pro Network</li>
      <li><span class="sq"></span>Blog</li>
    </ul>
  </div>
</footer>

</body>
</html>
```